Recycling company need a brochure - We are metal and electronic recycling company, we need a broc...

We need to illustrate our e-scrap services and values to our costumers in this brochure. We are collecting and recycling electronic waste. We are sorting, and dismanteling the goods to maximize value of the goods. We are using color green on business cards and on our trucks and containers, so brochure should also have green, we are a green business. It should communicate that doing business with us is; simple, easy to establish relations, quick transport service and
enviromental friendly. More info: www.vandelholm.dk

Target Market(s)

Companies with used electronic for scrap / Try go to www.vandelholm.dk to get more info.

Industry/Entity Type

Recycling

Font styles to use
Serif

Requirements
Must have
• Key services:
• Pick up service / Logistics
• Fast report
• Data destruction
• Fast payment
• AAA Credit-logo
• ISO14001 Certifikat-logo
• Company Logo
Nice to have
• Please browse the uploaded pictures, and use your favourites

```html
<!DOCTYPE html>
<html lang="en">
<head>
<meta charset="utf-8">
<title>Halvard Recycling Company – Brochure</title>
<link href="https://fonts.googleapis.com/css2?family=Oswald:wght@500;600;700&family=Open+Sans:wght@400;600;700&display=swap" rel="stylesheet">
<style>
:root{
  --green:#1f8a3f;
  --green-dark:#0f5e2a;
  --green-deep:#0b4a21;
  --green-light:#e6f2e9;
  --ink:#3a3a3a;
  --muted:#5f5f5f;
  --paper:#ffffff;
  --stage:#e4e6e5;
}
*{box-sizing:border-box;margin:0;padding:0}
html,body{width:1200px;height:2532px;overflow:hidden}
body{background:var(--stage);font-family:"Open Sans",Arial,sans-serif;color:var(--ink);
  display:flex;flex-direction:column;align-items:center;justify-content:center;gap:90px}
.spread{width:1100px;height:1100px;display:flex;background:var(--paper);box-shadow:0 6px 24px rgba(0,0,0,.18)}
.panel{width:33.3333%;height:100%;display:flex;flex-direction:column;position:relative;overflow:hidden;border-right:1px solid #e2e2e2}
.panel:last-child{border-right:none}
.panel-body{padding:30px 28px 22px;display:flex;flex-direction:column;gap:14px}
.heading{font-family:"Oswald",Arial,sans-serif;font-weight:600;font-size:32px;color:var(--green);letter-spacing:.5px;text-align:center;text-transform:uppercase}
.intro{font-weight:700;font-size:15px;line-height:1.45;color:var(--green-dark)}
.text{font-size:13px;line-height:1.6;color:var(--muted)}
.callout{background:var(--green);color:#fff;text-align:center;padding:14px;font-family:"Oswald",Arial,sans-serif;font-weight:500;font-size:19px;line-height:1.35}
.ticks{list-style:none;display:flex;flex-direction:column;gap:10px}
.ticks li{display:flex;gap:10px;font-size:13px;line-height:1.45;color:var(--ink);align-items:flex-start}
.ticks svg{flex:0 0 20px;margin-top:1px}
.photo{width:100%;flex:1 1 auto;min-height:120px}
.footer{height:52px;flex:0 0 52px;background:var(--green);color:#fff;display:flex;align-items:center;justify-content:center;font-weight:600;font-size:15px;letter-spacing:.3px}
.footer-band{border-top:6px solid var(--green-light)}
.panel--about{background:var(--green)}
.panel--about .panel-body{flex:1}
.panel--about .heading{color:#fff}
.panel--about .text{color:#e4f1e7}
.panel--about .footer{background:var(--green-deep)}
.brand{display:flex;flex-direction:column;align-items:center;gap:8px}
.brand-mark{width:44px;height:44px;border-radius:50%;background:var(--green)}
.brand-name{font-family:"Oswald",Arial,sans-serif;font-weight:600;font-size:22px;color:var(--green);text-transform:uppercase;text-align:center;line-height:1.15}
.panel--about .brand-mark{background:#fff}
.panel--about .brand-name{color:#fff}
.contact-title{font-family:"Oswald",Arial,sans-serif;font-weight:600;font-size:26px;color:#fff;text-align:center}
.contact-icons{display:flex;justify-content:center;gap:14px}
.contact-icons span{width:38px;height:38px;border-radius:50%;border:2px solid #fff;display:flex;align-items:center;justify-content:center}
.address{text-align:center;color:#fff;font-size:14px;line-height:1.6;font-weight:600}
.cover-art{position:absolute;left:0;top:0;width:100%;height:700px}
.cover-photo{position:absolute;left:48px;top:170px;width:300px;height:300px;border-radius:50%}
.cover-title{position:absolute;left:0;right:0;top:740px;text-align:center}
.welcome{font-family:"Oswald",Arial,sans-serif;font-weight:500;font-size:24px;color:var(--green)}
.cover-name{font-family:"Oswald",Arial,sans-serif;font-weight:700;font-size:64px;line-height:1;color:var(--green-dark);text-transform:uppercase;margin-top:6px}
.cover-sub{font-family:"Oswald",Arial,sans-serif;font-weight:600;font-size:24px;color:var(--green-dark);text-transform:uppercase;letter-spacing:1px;margin-top:4px}
.panel--cover .footer{position:absolute;left:0;right:0;bottom:0}
.head-band{background:var(--green-light);padding:20px 0 16px;border-bottom:4px solid var(--green);flex:0 0 auto}
.circles{display:flex;justify-content:center;gap:18px;padding:0 28px 24px}
.circle-photo{width:140px;height:140px;border-radius:50%;border:5px solid var(--green)}
.spacer{flex:1}
.footer-url{font-size:15px}
</style>
</head>
<body>

<section class="spread spread--outside">
  <article class="panel panel--solutions">
    <div class="panel-body">
      <h2 class="heading">Our Solutions</h2>
      <p class="intro">We collect, sort and recycle electronic scrap for companies of every size.</p>
      <p class="text">Our team dismantles each item by hand to recover metals and parts, so you get the best value while waste stays out of landfill. One call sets up a lasting partnership.</p>
      <div class="callout">Since 2011 we have served over 400 business clients</div>
      <p class="text">From office computers to industrial machines, we take care of the whole chain. Our experienced staff plan every collection, sort the goods on site and return a clear overview of what was recovered and what it is worth.</p>
      <ul class="ticks">
        <li><svg width="20" height="20" viewBox="0 0 20 20"><circle cx="10" cy="10" r="10" fill="#1f8a3f"/><path d="M5.5 10.2l3 3 6-6.4" stroke="#fff" stroke-width="2.2" fill="none"/></svg>Pick up service and logistics right at your door</li>
        <li><svg width="20" height="20" viewBox="0 0 20 20"><circle cx="10" cy="10" r="10" fill="#1f8a3f"/><path d="M5.5 10.2l3 3 6-6.4" stroke="#fff" stroke-width="2.2" fill="none"/></svg>Fast report on every single load we receive</li>
        <li><svg width="20" height="20" viewBox="0 0 20 20"><circle cx="10" cy="10" r="10" fill="#1f8a3f"/><path d="M5.5 10.2l3 3 6-6.4" stroke="#fff" stroke-width="2.2" fill="none"/></svg>Certified data destruction and fast payment</li>
      </ul>
    </div>
    <div class="photo" role="img" aria-label="Photo of a large pile of mixed electronic and metal scrap" style="background:linear-gradient(160deg,#8a8f92,#4d5356 55%,#6e6a5c)"></div>
    <div class="footer">www.halvardrecycling.example</div>
  </article>

  <article class="panel panel--about">
    <div class="panel-body">
      <h2 class="heading">About Us</h2>
      <p class="text">We are a metal and electronic recycling company. We collect used electronics from businesses and give every part a second life through careful sorting and dismantling.</p>
      <p class="text">Working with us is simple. Our drivers arrive quickly with green trucks and containers, and you receive a clear report and payment without delay or paperwork.</p>
      <p class="text">Green is more than our colour. We follow strict environmental standards and handle sensitive data safely from pick up to final processing.</p>
      <div class="brand" style="margin-top:14px">
        <span class="brand-mark"></span>
        <span class="brand-name">Halvard<br>Recycling Company</span>
      </div>
      <h3 class="contact-title" style="margin-top:10px">Contact Us</h3>
      <div class="contact-icons">
        <span><svg width="18" height="18" viewBox="0 0 24 24"><path d="M12 2a7 7 0 0 0-7 7c0 5 7 13 7 13s7-8 7-13a7 7 0 0 0-7-7zm0 9.5a2.5 2.5 0 1 1 0-5 2.5 2.5 0 0 1 0 5z" fill="#fff"/></svg></span>
        <span><svg width="18" height="18" viewBox="0 0 24 24"><path d="M6.6 10.8a15 15 0 0 0 6.6 6.6l2.2-2.2c.3-.3.7-.4 1-.2 1.1.4 2.3.6 3.6.6.6 0 1 .4 1 1V20c0 .6-.4 1-1 1A17 17 0 0 1 3 4c0-.6.4-1 1-1h3.5c.6 0 1 .4 1 1 0 1.3.2 2.5.6 3.6.1.3 0 .7-.2 1z" fill="#fff"/></svg></span>
        <span><svg width="18" height="18" viewBox="0 0 24 24"><rect x="3" y="5" width="18" height="14" rx="2" fill="none" stroke="#fff" stroke-width="2"/><path d="M3 7l9 6 9-6" fill="none" stroke="#fff" stroke-width="2"/></svg></span>
      </div>
      <p class="address">100 Sample Road, Suite 1, Greenfield<br>+00 000 000 0000<br>info@halvardrecycling.example</p>
    </div>
    <div class="footer">www.halvardrecycling.example</div>
  </article>

  <article class="panel panel--cover">
    <svg class="cover-art" viewBox="0 0 367 700" preserveAspectRatio="none" aria-hidden="true">
      <path d="M0 0H367V560C300 620 200 650 110 600C40 560 0 480 0 420Z" fill="#0f5e2a"/>
      <path d="M0 0H367V520C300 585 210 610 125 565C55 527 10 455 0 390Z" fill="#1f8a3f"/>
      <path d="M0 0H367V120C250 90 120 110 0 170Z" fill="#ffffff" opacity=".12"/>
    </svg>
    <div class="cover-photo" role="img" aria-label="Photo of used household appliances and electronics for recycling" style="background:radial-gradient(circle at 40% 35%,#f4f6f6,#c9cfd1 60%,#9aa3a6);border:8px solid #fff"></div>
    <div class="cover-title">
      <p class="welcome">Welcome to</p>
      <p class="cover-name">Halvard</p>
      <p class="cover-sub">Recycling Company</p>
    </div>
    <div class="footer">www.halvardrecycling.example</div>
  </article>
</section>

<section class="spread spread--inside">
  <article class="panel">
    <div class="head-band"><h2 class="heading">Heading One</h2></div>
    <div class="panel-body">
      <p class="intro">Pick up service and logistics planned around your schedule.</p>
      <p class="text">Book a collection and our truck arrives fast. We bring the right containers, load the goods safely and keep you updated until everything reaches our sorting hall.</p>
      <p class="text">Regular clients can choose fixed weekly routes, while one-off jobs are handled within a few working days. Every load is tracked and weighed on arrival.</p>
      <ul class="ticks">
        <li><svg width="20" height="20" viewBox="0 0 20 20"><circle cx="10" cy="10" r="10" fill="#1f8a3f"/><path d="M5.5 10.2l3 3 6-6.4" stroke="#fff" stroke-width="2.2" fill="none"/></svg>Quick transport with our own green fleet</li>
        <li><svg width="20" height="20" viewBox="0 0 20 20"><circle cx="10" cy="10" r="10" fill="#1f8a3f"/><path d="M5.5 10.2l3 3 6-6.4" stroke="#fff" stroke-width="2.2" fill="none"/></svg>Containers placed where you need them</li>
        <li><svg width="20" height="20" viewBox="0 0 20 20"><circle cx="10" cy="10" r="10" fill="#1f8a3f"/><path d="M5.5 10.2l3 3 6-6.4" stroke="#fff" stroke-width="2.2" fill="none"/></svg>One contact person for every order</li>
      </ul>
    </div>
    <div class="photo" role="img" aria-label="Photo of sorted circuit boards and cables" style="background:linear-gradient(150deg,#7d7a6c,#a89a78 45%,#5d6a5f)"></div>
    <div class="footer footer-band">www.halvardrecycling.example</div>
  </article>

  <article class="panel">
    <div class="head-band"><h2 class="heading">Heading Two</h2></div>
    <div class="panel-body">
      <p class="intro">Fast report and fast payment after every delivery.</p>
      <p class="text">Each load is weighed, sorted and dismantled to recover the highest value. You receive a clear report within days and payment follows straight after.</p>
      <p class="text">Our reports list weights, material groups and prices, so your accounts and environmental records stay complete without extra work on your side.</p>
      <ul class="ticks">
        <li><svg width="20" height="20" viewBox="0 0 20 20"><circle cx="10" cy="10" r="10" fill="#1f8a3f"/><path d="M5.5 10.2l3 3 6-6.4" stroke="#fff" stroke-width="2.2" fill="none"/></svg>Transparent prices for metals and parts</li>
        <li><svg width="20" height="20" viewBox="0 0 20 20"><circle cx="10" cy="10" r="10" fill="#1f8a3f"/><path d="M5.5 10.2l3 3 6-6.4" stroke="#fff" stroke-width="2.2" fill="none"/></svg>Strong credit rating you can trust</li>
      </ul>
    </div>
    <div class="spacer"></div>
    <div class="brand" style="margin-bottom:24px">
      <span class="brand-mark"></span>
      <span class="brand-name">Halvard<br>Recycling Company</span>
    </div>
    <div class="circles">
      <div class="circle-photo" role="img" aria-label="Photo of dismantled metal components" style="background:radial-gradient(circle,#b9b3a2,#6d6a60)"></div>
      <div class="circle-photo" role="img" aria-label="Photo of stacked electronic waste" style="background:radial-gradient(circle,#a7aeb1,#4f585c)"></div>
    </div>
    <div class="footer footer-band">www.halvardrecycling.example</div>
  </article>

  <article class="panel">
    <div class="head-band"><h2 class="heading">Heading Three</h2></div>
    <div class="panel-body">
      <p class="intro">Data destruction handled with care and full documentation.</p>
      <p class="text">Hard drives and storage media are wiped or shredded under controlled conditions. Our certified process protects your company and respects the environment at every step.</p>
      <p class="text">Sealed containers keep your devices secure from collection to destruction, and each serial number can be listed in the final certificate on request.</p>
      <ul class="ticks">
        <li><svg width="20" height="20" viewBox="0 0 20 20"><circle cx="10" cy="10" r="10" fill="#1f8a3f"/><path d="M5.5 10.2l3 3 6-6.4" stroke="#fff" stroke-width="2.2" fill="none"/></svg>Certificate issued for every batch</li>
        <li><svg width="20" height="20" viewBox="0 0 20 20"><circle cx="10" cy="10" r="10" fill="#1f8a3f"/><path d="M5.5 10.2l3 3 6-6.4" stroke="#fff" stroke-width="2.2" fill="none"/></svg>Environmental management standards</li>
        <li><svg width="20" height="20" viewBox="0 0 20 20"><circle cx="10" cy="10" r="10" fill="#1f8a3f"/><path d="M5.5 10.2l3 3 6-6.4" stroke="#fff" stroke-width="2.2" fill="none"/></svg>Secure storage until final processing</li>
      </ul>
    </div>
    <div class="photo" role="img" aria-label="Photo of scrap appliances and electronics heaped together" style="background:linear-gradient(165deg,#c7c9c6,#8e918c 50%,#5f6560)"></div>
    <div class="footer footer-band">www.halvardrecycling.example</div>
  </article>
</section>

</body>
</html>
```